Korvane Pty Ltd professional business card

A professional business card template using the colours from the supplied logo.
Clean crisp lines while, Modern while not being over the top.

Target Market(s)

Construction, commerical and industrial

Industry/Entity Type

Communications

Contact Information for Business Card

For a Communications, IT, Optical fibre installation company

Colors
37b8a4

```html
<!DOCTYPE html>
<html lang="en">
<head>
<meta charset="utf-8">
<title>Korvane Pty Ltd — Business Card</title>
<link href="https://fonts.googleapis.com/css2?family=Roboto:wght@400;500;700&display=swap" rel="stylesheet">
<style>
  :root {
    --teal: #37b8a4;
    --teal-light: #4cc2af;
    --teal-deep: #1f7f8c;
    --ink: #55565a;
    --ink-dark: #333438;
    --paper: #ffffff;
    --backdrop: #ebe9e6;
  }
  * { box-sizing: border-box; margin: 0; padding: 0; }
  html, body {
    width: 1200px; height: 961px; overflow: hidden;
    background: var(--backdrop);
    font-family: "Roboto", Arial, sans-serif;
  }
  .canvas { position: relative; width: 1200px; height: 961px; }

  .card {
    position: absolute;
    width: 620px; height: 354px;
    box-shadow: 0 10px 28px rgba(0,0,0,0.12);
    overflow: hidden;
  }

  /* Front */
  .card-front { left: 90px; top: 90px; background: var(--teal); }
  .card-front .map-area {
    position: absolute; left: 50px; top: 30px; width: 520px; height: 290px;
    background: radial-gradient(ellipse at center, var(--teal-light) 0%, var(--teal) 70%);
    border-radius: 40px;
  }
  .card-front .brand {
    position: absolute; left: 0; right: 0; top: 50%;
    transform: translateY(-50%);
    display: flex; align-items: center; justify-content: center; gap: 18px;
    color: var(--paper);
    font-weight: 500; font-size: 76px; letter-spacing: 4px;
  }
  .card-front .brand-dot {
    width: 34px; height: 34px; border-radius: 50%; background: var(--paper);
  }

  /* Back */
  .card-back { left: 490px; top: 517px; background: var(--paper); }
  .card-back .brand {
    position: absolute; right: 48px; top: 44px;
    display: flex; align-items: center; gap: 12px;
    color: var(--ink);
    font-weight: 500; font-size: 44px; letter-spacing: 3px;
  }
  .card-back .brand-dot {
    width: 22px; height: 22px; border-radius: 50%; background: var(--teal-deep);
  }
  .address {
    position: absolute; right: 48px; top: 150px;
    text-align: right; color: var(--ink);
    font-size: 15px; line-height: 22px;
  }
  .accent-bar {
    position: absolute; left: 0; top: 212px; width: 12px; height: 34px;
    background: var(--teal-deep);
  }
  .person { position: absolute; left: 40px; top: 196px; }
  .person-name {
    color: var(--teal-deep); font-weight: 700; font-size: 20px; letter-spacing: 0.5px;
  }
  .person-role {
    color: var(--ink-dark); font-weight: 500; font-size: 14px; margin-top: 2px;
  }
  .contacts { list-style: none; margin-top: 14px; }
  .contacts li {
    display: flex; align-items: center; gap: 10px;
    color: var(--ink); font-size: 16px; line-height: 24px;
  }
  .contacts svg { width: 14px; height: 14px; flex: none; }
</style>
</head>
<body>
<div class="canvas">

  <section class="card card-front">
    <div class="map-area" role="img" aria-label="Faint dotted world map pattern"></div>
    <div class="brand"><span class="brand-dot"></span>KORVANE</div>
  </section>

  <section class="card card-back">
    <div class="brand"><span class="brand-dot"></span>KORVANE</div>

    <p class="address">48 Larkfield Crescent,<br>Ashbury, ON K2T 4P7</p>

    <div class="accent-bar"></div>
    <div class="person">
      <p class="person-name">MARCUS BELDEN</p>
      <p class="person-role">Managing Director</p>
      <ul class="contacts">
        <li>
          <svg viewBox="0 0 16 16"><path fill="#1f7f8c" d="M3 1h3l1 4-2 1a9 9 0 0 0 5 5l1-2 4 1v3c0 1-1 2-2 2C7 15 1 9 1 3c0-1 1-2 2-2z"/></svg>
          +15550143927
        </li>
        <li>
          <svg viewBox="0 0 16 16"><rect x="1" y="3" width="14" height="10" rx="1" fill="#1f7f8c"/><path d="M1.5 4l6.5 5 6.5-5" stroke="#fff" stroke-width="1.4" fill="none"/></svg>
          marcus@korvane.net
        </li>
        <li>
          <svg viewBox="0 0 16 16"><circle cx="8" cy="8" r="6.5" stroke="#1f7f8c" stroke-width="1.4" fill="none"/><path d="M1.5 8h13M8 1.5c-3 3.5-3 9.5 0 13M8 1.5c3 3.5 3 9.5 0 13" stroke="#1f7f8c" stroke-width="1.2" fill="none"/></svg>
          www.korvane.net
        </li>
      </ul>
    </div>
  </section>

</div>
</body>
</html>
```